Cash Back to Home Buyers Flyer

We need a flyer for Brisk Haven real estate brokerage advertising Money Saving Offer to Home buyers - Cash Back Rebate and explaining how the concept works. The design should communicate how that money saving offer works and should motivate buyers to take advantage of it. Feel free to edit the text based on the attached designs and use infographics.

Target Market(s)

Middle aged professionals

Industry/Entity Type

Real Estate

Requirements
Must have
• Call to action highlights, Dollar signs. Graphics to show rebate math as in the attached file.

```html
<!DOCTYPE html>
<html lang="en">
<head>
<meta charset="utf-8">
<title>Brisk Haven – Home Buyers Cash Back Rebate</title>
<link rel="stylesheet" href="https://fonts.googleapis.com/css2?family=Montserrat:wght@400;500;600;700;800&family=Lora:wght@400&family=Oswald:wght@600&display=swap">
<style>
  :root{
    --teal:#12b5a6;
    --teal-bright:#1fd8c6;
    --teal-deep:#05776d;
    --cyan:#3fe6d4;
    --ink:#2b2b2b;
    --grey:#8a8a8a;
    --grey-light:#dcdcdc;
    --backdrop:#b4b4b4;
    --paper:#ffffff;
  }
  *{margin:0;padding:0;box-sizing:border-box}
  html,body{width:800px;height:1200px;overflow:hidden;background:var(--backdrop)}
  body{font-family:"Montserrat",Arial,sans-serif;color:var(--ink)}
  .flyer{position:absolute;left:0;top:34px;width:800px;height:1132px;background:var(--paper);overflow:hidden}
  .flyer-shapes{position:absolute;inset:0}
  .t{position:absolute;white-space:nowrap}
  .brand{left:145px;top:90px;font-family:"Lora",Georgia,serif;font-size:28px;color:var(--grey)}
  .brand-mark{position:absolute;left:48px;top:48px;width:62px;height:62px;border:5px solid var(--teal)}
  .hero-kicker{left:45px;top:216px;font-size:44px;font-weight:400;color:#fff;letter-spacing:.5px}
  .hero-title{left:45px;top:262px;font-size:48px;font-weight:800;color:#fff;letter-spacing:1px}
  .hero-title.big{top:314px;font-size:64px}
  .hero-tag{left:45px;top:424px;font-size:34px;font-weight:700;color:var(--cyan);letter-spacing:1px}
  .hero-sub{left:45px;top:460px;font-size:32px;font-weight:400;color:#fff}
  .h2{font-size:36px;font-weight:400;color:var(--ink)}
  .h2 b{color:var(--teal);font-weight:800}
  .h3{font-size:23px;font-weight:400;color:var(--ink);line-height:28px}
  .h3 b{display:block;color:var(--teal);font-weight:700}
  .copy{font-size:14px;line-height:17.6px;color:var(--ink);white-space:normal}
  .copy b{color:var(--teal);font-weight:700}
  .checks{list-style:none;left:425px;top:722px}
  .checks li{font-size:13px;font-weight:700;height:32.6px;padding-left:19px;position:relative}
  .checks li::before{content:"";position:absolute;left:2px;top:3px;width:10px;height:10px;border:1px solid var(--grey);border-radius:50%}
  .checks li::after{content:"";position:absolute;left:5px;top:5px;width:3px;height:5px;border:solid var(--grey);border-width:0 1px 1px 0;transform:rotate(40deg)}
  .rebate-label{left:72px;top:744px;font-size:14px;color:#fff}
  .rebate-note{left:72px;top:772px;font-size:12px;line-height:11px;color:#444}
  .pct{left:258px;top:735px;width:78px;text-align:center;font-family:"Oswald",Impact,sans-serif;font-weight:600;font-size:40px;color:#fff;line-height:44px}
  .pct-note{left:258px;top:783px;width:78px;text-align:center;font-size:8px;line-height:10px;color:#fff;white-space:normal}
  .plan-tab{left:450px;top:826px;width:280px;font-size:14px;font-weight:600;color:var(--ink)}
  .plan-price{left:440px;top:852px;font-size:16px;font-weight:500}
  .plan-price .amt{font-family:"Oswald",Impact,sans-serif;font-size:22px;font-weight:600}
  .plan-price sup{font-size:12px;font-weight:700}
  .save{left:425px;top:902px;font-size:23px;font-weight:800;color:var(--teal);line-height:26px}
  .save span{display:block;color:var(--ink);font-weight:400}
  .phone{left:88px;top:1065px;font-size:30px;font-weight:700;color:#fff}
  .email{left:88px;top:1101px;font-size:20px;font-weight:400;color:#fff}
  .web{left:474px;top:1066px;font-size:16px;color:var(--ink)}
</style>
</head>
<body>
<main class="flyer">
  <svg class="flyer-shapes" width="800" height="1132" viewBox="0 0 800 1132" aria-hidden="false">
    <defs>
      <linearGradient id="heroGrad" x1="0" y1="0" x2="0" y2="1">
        <stop offset="0" stop-color="#15d3c0"/>
        <stop offset="1" stop-color="#05756b"/>
      </linearGradient>
      <linearGradient id="photoGrad" x1="0" y1="0" x2="0" y2="1">
        <stop offset="0" stop-color="#5f9de8"/>
        <stop offset=".45" stop-color="#c9d3e0"/>
        <stop offset=".75" stop-color="#5f7fa6"/>
        <stop offset="1" stop-color="#2f5a2a"/>
      </linearGradient>
      <linearGradient id="footGrad" x1="0" y1="0" x2="1" y2="0">
        <stop offset="0" stop-color="#0aa698"/>
        <stop offset="1" stop-color="#20d8c5"/>
      </linearGradient>
    </defs>
    <!-- header rule -->
    <line class="header-rule" x1="0" y1="152" x2="340" y2="152" stroke="#8a8a8a" stroke-width="4"/>
    <!-- hero teal panel -->
    <polygon class="hero-panel" points="0,161 346,161 505,544 0,544" fill="url(#heroGrad)"/>
    <!-- hero photo -->
    <polygon class="hero-photo" role="img" aria-label="Photo of a large stone luxury house lit at dusk with front steps and landscaped garden"
      points="469,37 800,37 800,544 517,544 346,161" fill="url(#photoGrad)"/>
    <line x1="332" y1="161" x2="464" y2="37" stroke="var(--teal)" stroke-width="5"/>
    <line x1="360" y1="270" x2="480" y2="544" stroke="#9a9a9a" stroke-width="5"/>
    <!-- hero divider -->
    <line x1="45" y1="398" x2="350" y2="398" stroke="#fff" stroke-width="1"/>
    <line x1="65" y1="398" x2="120" y2="398" stroke="#fff" stroke-width="6" stroke-linecap="round"/>
    <!-- section band -->
    <line x1="0" y1="558" x2="800" y2="558" stroke="#8a8a8a" stroke-width="5"/>
    <polygon points="572,548 650,548 645,556 567,556" fill="var(--teal)"/>
    <polygon points="662,548 740,548 735,556 657,556" fill="var(--teal)"/>
    <polygon points="752,548 800,548 800,556 747,556" fill="var(--teal)"/>
    <!-- About underline -->
    <line x1="48" y1="644" x2="130" y2="644" stroke="#8a8a8a" stroke-width="1"/>
    <line x1="58" y1="644" x2="95" y2="644" stroke="var(--teal)" stroke-width="5" stroke-linecap="round"/>
    <!-- rebate graphic -->
    <rect x="48" y="740" width="250" height="24" rx="10" fill="var(--teal)"/>
    <rect x="48" y="764" width="250" height="32" fill="var(--grey-light)"/>
    <circle cx="297" cy="768" r="49" fill="#fff"/>
    <circle cx="297" cy="768" r="46" fill="var(--teal)"/>
    <circle cx="297" cy="768" r="41" fill="none" stroke="#fff" stroke-width="1.5" stroke-dasharray="2 3"/>
    <!-- right column underlines -->
    <line x1="425" y1="648" x2="500" y2="648" stroke="#8a8a8a" stroke-width="1"/>
    <line x1="430" y1="648" x2="465" y2="648" stroke="var(--teal)" stroke-width="5" stroke-linecap="round"/>
    <line x1="425" y1="970" x2="500" y2="970" stroke="#8a8a8a" stroke-width="1"/>
    <line x1="430" y1="970" x2="465" y2="970" stroke="var(--teal)" stroke-width="5" stroke-linecap="round"/>
    <!-- plan box -->
    <rect x="425" y="824" width="318" height="66" rx="8" fill="var(--grey-light)"/>
    <rect x="428" y="824" width="306" height="24" rx="8" fill="var(--teal-bright)"/>
    <!-- footer -->
    <polygon class="footer-band" points="0,1045 380,1045 450,1132 0,1132" fill="url(#footGrad)"/>
    <line x1="455" y1="1117" x2="800" y2="1117" stroke="#8a8a8a" stroke-width="5"/>
    <line x1="460" y1="1126" x2="800" y2="1126" stroke="var(--teal)" stroke-width="4"/>
    <!-- phone icon -->
    <path d="M50 1072 q-3 4 2 12 q6 10 14 12 l4 -4 -6 -5 -3 3 q-5 -3 -8 -9 l3 -3 -4 -6z" fill="#fff"/>
    <!-- mail icon -->
    <rect x="50" y="1106" width="18" height="12" fill="none" stroke="#fff" stroke-width="1.5"/>
    <path d="M50 1106 l9 7 9 -7" fill="none" stroke="#fff" stroke-width="1.5"/>
    <!-- globe icon -->
    <circle cx="464" cy="1076" r="9" fill="none" stroke="var(--teal)" stroke-width="2"/>
    <ellipse cx="464" cy="1076" rx="4" ry="9" fill="none" stroke="var(--teal)" stroke-width="1.5"/>
    <line x1="455" y1="1076" x2="473" y2="1076" stroke="var(--teal)" stroke-width="1.5"/>
  </svg>

  <div class="brand-mark" aria-hidden="true"></div>
  <div class="t brand">Brisk Haven</div>

  <div class="t hero-kicker">Home Buyers</div>
  <div class="t hero-title">CASH BACK</div>
  <div class="t hero-title big">REBATE</div>
  <div class="t hero-tag">DISCOUNTED</div>
  <div class="t hero-sub">Real Estate Services</div>

  <h2 class="t h2" style="left:48px;top:595px">About <b>Us</b></h2>
  <p class="t copy" style="left:48px;top:664px;width:330px">If you are buying or planning to buy a property in NJ this information can make a big difference for you.</p>
  <div class="t rebate-label">You can get up to</div>
  <div class="t rebate-note">back in your pocket<br>at closing</div>
  <div class="t pct">2%</div>
  <div class="t pct-note">of Selling<br>price</div>
  <p class="t copy" style="left:48px;top:829px;width:330px">Average rebate we pay for a <b>$500,000</b> home sale is about <b>$7,500</b>! The same great level of service,professional advice and guidance PLUS a huge check at your closing to cover your closing costs!</p>
  <p class="t copy" style="left:48px;top:938px;width:300px">All commissions are negotiable in NJ. Consult a tax professional regarding a receipt of the rebate.</p>
  <p class="t copy" style="left:48px;top:1004px"><b>Location:</b> New Jersey</p>

  <h3 class="t h3" style="left:425px;top:582px">MLS Listing Plans<b>For Sale By Owner</b></h3>
  <h3 class="t h3" style="left:425px;top:662px">Best Alternative to<b>FSBO Sales</b></h3>
  <ul class="t checks">
    <li>Greater Exposure</li>
    <li>Professional Advise</li>
    <li>Agent Hosted Open Houses</li>
  </ul>
  <div class="t plan-tab" style="text-align:center">Get More Buyers - Sell for More!</div>
  <div class="t plan-price">Listing Plans Start at only <sup>$</sup><span class="amt">359</span></div>
  <div class="t save">SAVE $$$<span>on Home Listing</span></div>
  <p class="t copy" style="left:425px;top:985px;width:340px">We sell homes quicker and for more money. And we charge for our services as low as <b>1.5-2%</b> in Listing Commission.</p>

  <div class="t phone">(555)014-2876</div>
  <div class="t email">info@briskhaven.example</div>
  <div class="t web">www.briskhaven.example</div>
</main>
</body>
</html>
```